QuadLantern--Help Us look fresh and new to companies, college students and college career centers!

We just designed a new logo and would like to freshen-up and make our business cards a bit more modern. Not crazy-modern like Picasso, but modern like metro-style and fresh like fruit. We use three logos with a combination of two colors each, and three colors total. We are looking for a single format to apply to three different cards/color schemes (green/blue to give out to companies, orange/green for students, and orange/blue for university career centers). Thanks everyone--looking forward to seeing your designs!!

Target Market(s)

Three styles: companies, college students/grads, college career centers

Industry/Entity Type

College

Contact Information for Business Card

Address: 1187 9th Avenue, Suite 614, Seattle, WA 98104. Need a spot for email address, web address (www.quadlantern-example.com), and phone numbers (main, direct, mobile). Don't open that website unless you want to lose your lunch--it is waaaay old and outdated. See this link instead, http://staging.brixelworks-example.com/QuadLantern/EmployerSolutions, for our new website design in progress.

Font styles to use
Sans Serif

Requirements
Must have
• Please use the logos supplied. Would like text to be grey but printable, like a "light" type style that is metro-type with sans-serif. NOT black text. Modern. For inspiration, here's a link to our work-in-progress website we are planning to launch soon: http://staging.brixelworks-example.com/QuadLantern/EmployerSolutions
Nice to have
• Would like to see something unique and different in a "metro" style. Clean and not cluttered.
Should not have
• No odd-sized cards

```html
<!DOCTYPE html>
<html lang="en">
<head>
<meta charset="utf-8">
<title>QuadLantern Business Cards</title>
<link rel="stylesheet" href="https://fonts.googleapis.com/css2?family=Exo+2:wght@300;400;600&display=swap">
<style>
  :root {
    --page: #eef0f2;
    --card-white: #f4f5f6;
    --brand-blue: #127dc2;
    --brand-green: #74bd43;
    --faint-blue: #cfe2ef;
    --faint-green: #e1eed8;
    --text-light: #ffffff;
  }
  * { margin: 0; padding: 0; box-sizing: border-box; }
  html, body { width: 1200px; height: 899px; overflow: hidden; }
  body {
    background: var(--page);
    font-family: "Exo 2", sans-serif;
    position: relative;
  }
  .card {
    position: absolute;
    left: 280px;
    width: 640px;
    height: 366px;
    background: var(--card-white);
    overflow: hidden;
    box-shadow: 0 6px 18px rgba(0,0,0,0.15);
  }
  .card-back { top: 50px; }
  .card-front { top: 483px; }
  .card-shapes { position: absolute; inset: 0; width: 100%; height: 100%; }

  .back-website {
    position: absolute;
    left: 22px;
    top: 186px;
    font-size: 12px;
    font-weight: 400;
    color: var(--text-light);
    letter-spacing: 0.3px;
    white-space: nowrap;
  }
  .back-mark {
    position: absolute;
    left: 300px;
    top: 120px;
    display: flex;
    align-items: center;
    gap: 12px;
  }
  .back-mark-dot {
    width: 60px; height: 60px;
    border-radius: 50%;
    background: var(--faint-green);
  }
  .back-mark-name {
    font-size: 36px;
    font-weight: 600;
    color: var(--faint-blue);
    white-space: nowrap;
  }

  .front-brand {
    position: absolute;
    left: 28px;
    top: 196px;
    display: flex;
    align-items: center;
    gap: 10px;
  }
  .brand-dot {
    width: 20px; height: 20px;
    border-radius: 50%;
    background: var(--brand-green);
  }
  .brand-name {
    font-size: 34px;
    font-weight: 600;
    color: var(--brand-blue);
    white-space: nowrap;
  }

  .contact-block {
    position: absolute;
    right: 28px;
    top: 28px;
    text-align: right;
    color: var(--text-light);
  }
  .person-name { font-size: 18px; font-weight: 400; letter-spacing: 1px; }
  .person-role { font-size: 13px; font-weight: 300; margin-top: 2px; }
  .address { font-size: 13px; font-weight: 300; margin-top: 34px; line-height: 1.4; }
  .contact-list { list-style: none; margin-top: 30px; font-size: 12.5px; font-weight: 300; }
  .contact-list li { display: flex; justify-content: flex-end; align-items: center; gap: 8px; height: 22px; white-space: nowrap; }
  .contact-list svg { width: 12px; height: 12px; fill: none; stroke: var(--text-light); stroke-width: 1.6; }
</style>
</head>
<body>

<section class="card card-back">
  <svg class="card-shapes" viewBox="0 0 640 366" aria-hidden="true">
    <polygon points="130,0 148,0 240,175 214,366 196,366 222,175" fill="var(--brand-green)"/>
    <polygon points="0,0 130,0 222,175 196,366 0,366" fill="var(--brand-blue)"/>
  </svg>
  <div class="back-mark">
    <span class="back-mark-dot"></span>
    <span class="back-mark-name">QuadLantern</span>
  </div>
  <p class="back-website">www.quadlantern-example.com</p>
</section>

<section class="card card-front">
  <svg class="card-shapes" viewBox="0 0 640 366" aria-hidden="true">
    <polygon points="210,0 640,0 640,366 300,366 335,150" fill="var(--brand-blue)"/>
    <polygon points="192,0 210,0 335,150 300,366 286,366 318,150" fill="var(--brand-green)"/>
  </svg>
  <div class="front-brand">
    <span class="brand-dot"></span>
    <span class="brand-name">QuadLantern</span>
  </div>
  <div class="contact-block">
    <p class="person-name">MARCUS ELLERY</p>
    <p class="person-role">Managing Director</p>
    <p class="address">1187 9th Avenue, Suite 614<br>Seattle, WA 98104</p>
    <ul class="contact-list">
      <li>206 555 0148
        <svg viewBox="0 0 12 12"><path d="M2 1h3l1 3-2 1a7 7 0 0 0 3 3l1-2 3 1v3a1 1 0 0 1-1 1A10 10 0 0 1 1 2a1 1 0 0 1 1-1z"/></svg></li>
      <li>206 555 0149
        <svg viewBox="0 0 12 12"><rect x="3" y="1" width="6" height="10" rx="1"/><path d="M5.5 9.5h1"/></svg></li>
      <li>206 555 0150
        <svg viewBox="0 0 12 12"><rect x="1" y="4" width="10" height="6"/><path d="M3 4V1h6v3"/></svg></li>
      <li>hello@quadlantern-example.com
        <svg viewBox="0 0 12 12"><rect x="1" y="2.5" width="10" height="7"/><path d="M1 2.5l5 4 5-4"/></svg></li>
      <li>www.quadlantern-example.com
        <svg viewBox="0 0 12 12"><circle cx="6" cy="6" r="5"/><path d="M1 6h10M6 1c-3 3-3 7 0 10M6 1c3 3 3 7 0 10"/></svg></li>
    </ul>
  </div>
</section>

</body>
</html>
```